Letterhead Design Project for online gaming site

We need a letterhead for a new online gaming company. The site is www.lunorapick.co

The logo is a gold colour and the site is similar in nature. Feel free to take a look at the landing page.

However the designer has free reign to do whatever they like with it.

OTHER CONTENT:

Telephone: 1300 617 385
Email: info@lunorapick.co
Web: www.lunorapick.co

Industry/Entity Type

It Company

```html
<!DOCTYPE html>
<html lang="en">
<head>
<meta charset="utf-8">
<title>LunoraPick.co Letterhead</title>
<link href="https://fonts.googleapis.com/css2?family=Arimo:wght@400;700&family=Libre+Baskerville&family=Roboto+Condensed:wght@400&display=swap" rel="stylesheet">
<style>
  :root {
    --bg-top: #c4c3c1;
    --bg-bottom: #f4f4f4;
    --paper: #ffffff;
    --gold: #d9a80b;
    --gold-dark: #ac8a2a;
    --band-start: #f7d414;
    --band-end: #8b7335;
    --ink: #3b3b3b;
    --ink-dark: #222222;
    --silhouette: #e6e6e6;
    --rule: #bdbdbd;
  }
  * { margin: 0; padding: 0; box-sizing: border-box; }
  html, body { width: 1200px; height: 750px; overflow: hidden; }
  body {
    position: relative;
    background: linear-gradient(180deg, var(--bg-top) 0%, var(--bg-bottom) 70%);
    font-family: "Arimo", Arial, sans-serif;
  }
  .sheet {
    position: absolute;
    width: 421px;
    height: 598px;
    background: var(--paper);
    box-shadow: 3px 5px 8px rgba(0,0,0,0.35);
  }
  .sheet--first { left: 180px; top: 75px; }
  .sheet--continuation { left: 655px; top: 77px; }

  .brand-name {
    position: absolute;
    font-family: "Arimo", Arial, sans-serif;
    font-weight: 700;
    color: var(--gold);
    letter-spacing: -0.5px;
    white-space: nowrap;
  }
  .sheet--first .brand-name { left: 16px; top: 17px; font-size: 30px; }
  .sheet--continuation .brand-name { right: 14px; top: 52px; font-size: 21px; }

  .contact {
    position: absolute;
    right: 28px;
    top: 21px;
    text-align: right;
    font-family: "Libre Baskerville", Georgia, serif;
    font-size: 7px;
    line-height: 10.5px;
    color: var(--ink-dark);
  }
  .contact .label { color: var(--gold-dark); }
  .edge-tab {
    position: absolute;
    right: 0; top: 19px;
    width: 9px; height: 43px;
    background: var(--gold-dark);
  }

  .letter {
    position: absolute;
    left: 25px;
    top: 154px;
    width: 384px;
    font-size: 6.6px;
    line-height: 15.6px;
    color: var(--ink);
  }
  .letter .greeting { font-weight: 700; color: var(--ink-dark); margin-bottom: 12px; }
  .letter p { margin-bottom: 12px; }

  .silhouette {
    position: absolute;
    background: linear-gradient(90deg, var(--silhouette), #ececec);
    border-radius: 40px 40px 6px 6px;
    opacity: 0.9;
  }
  .sheet--first .silhouette { left: 26px; top: 468px; width: 340px; height: 100px; }
  .sheet--continuation .silhouette { left: 16px; top: 12px; width: 210px; height: 66px; }

  .header-rule {
    position: absolute;
    left: 15px; right: 14px; top: 79px;
    height: 2px;
    background: var(--rule);
  }
  .page-count {
    position: absolute;
    right: 18px; top: 20px;
    font-family: "Libre Baskerville", Georgia, serif;
    font-size: 7.5px;
    color: #555;
  }

  .service-band {
    position: absolute;
    left: 0; right: 0; bottom: 0;
    height: 23px;
    background: linear-gradient(90deg, var(--band-start) 0%, var(--band-start) 25%, var(--band-end) 100%);
    display: flex;
    align-items: center;
    padding-left: 29px;
    font-family: "Roboto Condensed", "Arial Narrow", sans-serif;
    font-size: 10px;
    letter-spacing: 2.2px;
    color: var(--ink-dark);
    white-space: nowrap;
  }
  .service-band .gap { display: inline-block; width: 6px; }
</style>
</head>
<body>

  <section class="sheet sheet--first" aria-label="Letterhead first page">
    <div class="brand-name">LunoraPick.co</div>
    <address class="contact" style="font-style:normal">
      <div><span class="label">Telephone:</span> 1300 617 385</div>
      <div><span class="label">Email:</span> info@lunorapick.co</div>
      <div><span class="label">Web:</span> www.lunorapick.co</div>
    </address>
    <div class="edge-tab"></div>

    <article class="letter">
      <p class="greeting">Dear Customer,</p>
      <p>Lorem ipsum dolor sit amet, consectetur adipiscing elit. Donec elementum velit sit amet libero fringilla adipiscing. Aliquam sollicitudin, leo vitae molestie facilisis, tellus ligula varius velit, vitae tincidunt lacus purus vitae nulla. Nulla imperdiet, odio quis ultrices ornare, diam est dictum lacus, et vehicula est magna at metus. Integer mattis lorem quis tortor accumsan ultrices ac ut massa. Duis eget metus ut risus scelerisque ornare quis eget dui. Aliquam lobortis dolor vitae magna volutpat eu facilisis tellus molestie. Sed a purus quis nibh lacinia interdum ut at leo.</p>
      <p>Integer consequat velit quis elit hendrerit imperdiet. Donec felis velit, volutpat vel convallis nec, sollicitudin et nulla. Pellentesque sodales elementum aliquam. Donec convallis, turpis sit amet laoreet ultricies, enim est elementum magna, dictum lobortis eros tellus quis diam. Nunc suscipit augue non nisl volutpat volutpat. Ut egestas ultrices purus, eget varius nibh placerat in. Cras leo ante, congue id ultricies a, ornare eu est. Curabitur eleifend tincidunt mi eget tristique.</p>
      <p>Etiam arcu augue, ornare vitae consectetur luctus, tincidunt vitae urna. Lorem ipsum dolor sit amet, consectetur adipiscing elit. Donec vitae tortor quis orci adipiscing lobortis. Morbi aliquet orci quis mi viverra sollicitudin. Sed eget pellentesque turpis. Aliquam commodo sodales ultrices. Nullam ut elit vitae elit suscipit porttitor viverra non mi. Donec diam mi, tincidunt nec sodales vestibulum, iaculis a urna. Nulla facilisi.</p>
      <p>Thanking you,</p>
    </article>

    <div class="silhouette" role="img" aria-label="Faint grey silhouettes of a harness racer, a jockey on a galloping horse, greyhounds and a football"></div>

    <footer class="service-band">THOROUGHBRED HARNESS GREYHOUND<span class="gap"></span> SPORT AND LAY BETTING</footer>
  </section>

  <section class="sheet sheet--continuation" aria-label="Letterhead continuation page">
    <div class="silhouette" role="img" aria-label="Faint grey silhouettes of a harness racer, galloping horses, greyhounds and a football"></div>
    <div class="page-count">Page:______Of_______</div>
    <div class="brand-name">LunoraPick.co</div>
    <div class="header-rule"></div>

    <footer class="service-band">THOROUGHBRED HARNESS GREYHOUND<span class="gap"></span> SPORT AND LAY BETTING</footer>
  </section>

</body>
</html>
```